Website Design Chair in Business Administration, especially logistics and trade networks

We, the Chair in Business Administration, especially logistics and trade networks, teach in the field of Business Informatics and Business Administration at Ostermark University.
We want to setup our current website in a fresh new and clean design because the design of the old page is outdated: http://ltn.uni-ostermark.example/en/
The design should be created in a way that we can integrate it into Wordpress later. Furthermore, the website should have the existing website tabs (pages). We want to add the missing subcategories in the tabs, which means that when you move the mouse over a tab, subcategories/side menus should appear.
We have the goal that the website is very clear and that the students get a direct overview especially of the lectures offered. Furthermore the website should be suitable for mobile devices.
Start page:
In general we are interested in a Tile-based Design (2 or more columns) on the start page - similar to this page: https://www.uni-bv.example/. Here, the fields (Logistics and Trade Networks (LTN) with photo, Lectures of the semester, theses, study projects, projects, current events (social media wall), jobs and internship (together), new publications) should be integrated in the form of tiles with a cover picture per field and a short description.
Furthermore, we would like to position a search bar, a social media wall especially for Pictoria (replaces the field current events) and the cooperation partners perhaps as sliders with logos of the companies in the lower part of the start page (see Cooperation tab on the far right) on the start page. Footer remains the same.
Research:
Display the same content more attractively.
Learning-Platform:
Furthermore only as link.
Teaching:
In addition to the existing sub-items (Lectures of the semester, teaching-archive, learning platform, theses and book lending), the "Overview of LTN courses" and the " Open Bachelor & Master theses" should be graphically displayed.
Team:
The concept of the Teamgraph including project connections should remain. Furthermore we can imagine to list the employees with photos and short description in form of tiles (1 employee on a tile) below the graph (2 or more columns of tiles).
Publications:
Continue to display a list of publications.
Jobs and internships:
The Open Positions should be divided here into Research Associates, Student Assistants and interns, so that it becomes clearer (3 columns).
Projects:
Here we are interested a Tile-based Design (2 or more columns). We want to integrate the project fields (QUINTAL, Harbor Cloud Ledger etc.) in the form of tiles with a title image per field and a short description.
Events and cooperations should be removed as they are sufficiently represented on the start page.
Target Market(s)
Students as well as current and future project partners
Logo Text
LTN (+ optional Chair in Logistics and Trade Networks)
Coding
Coded - Design and coding required
Number of Pages Required
5+ page
Requirements
Must have
- See description above
Nice to have
- Perhaps a design can be created in which a direct connection to research content (AI, Deep Learning etc.) and to courses (Data Science, AI in companies etc.) can be seen.

```html
<!DOCTYPE html>
<html lang="en">
<head>
<meta charset="utf-8">
<title>Logistics and Trade Networks (LTN)</title>
<link href="https://fonts.googleapis.com/css2?family=Montserrat:wght@400;500&display=swap" rel="stylesheet">
<style>
:root{
  --red:#ec1c24;
  --red-soft:#f46a6e;
  --pink:#f39194;
  --grey-bg:#efefef;
  --navy:#1f4e8c;
  --blue:#2a6cb0;
  --sky:#2f9fd8;
  --ice:#cfe8f8;
  --pub-blue:#2a73c2;
  --deep:#142a52;
  --dark:#252525;
  --edge:#111;
  --footer:#bdbdbd;
  --ink:#222;
  --icon:#444;
  --brand:#2a5da8;
}
*{box-sizing:border-box;margin:0;padding:0}
html,body{width:1200px;height:3650px;overflow:hidden}
body{font-family:'Montserrat',sans-serif;color:var(--ink);background:var(--edge);position:relative}
.site-header{position:absolute;left:0;top:0;width:1200px;height:81px;background:#fff}
.brand{position:absolute;left:44px;top:24px;display:flex;align-items:center;gap:6px}
.brand-mark{width:13px;height:13px;background:var(--brand)}
.brand-name{font-size:22px;font-weight:500;color:var(--brand);line-height:1}
.main-nav{position:absolute;left:130px;top:27px;display:flex;gap:18px;font-size:13px;color:#333}
.main-nav svg{margin-top:2px}
.university{position:absolute;left:910px;top:16px;display:flex;align-items:center;gap:10px}
.university-mark{width:40px;height:40px;border-radius:50%;background:var(--brand)}
.university-name{font-size:11px;font-weight:500;color:var(--brand);line-height:1.35}
.hero{position:absolute;left:0;top:81px;width:1200px;height:359px;background:#fff}
.hero-photo{position:absolute;left:0;top:0;width:906px;height:359px;background:linear-gradient(110deg,#c9c4b6,#9fa58e 40%,#e4e6ea 60%,#b9b8ae)}
.hero-intro{position:absolute;left:0;top:0;width:444px;height:359px;background:rgba(240,236,226,.72);padding:30px 16px;text-align:center}
.hero-intro h1{font-size:22px;font-weight:400;line-height:1.25;margin-bottom:24px}
.hero-intro p{font-size:10.5px;line-height:1.3;margin-bottom:22px}
.hero-side{position:absolute;left:906px;width:251px;height:170px}
.hero-side.top{top:4px;background:linear-gradient(135deg,#6d6a60,#b9b6aa,#5a5d55)}
.hero-side.bottom{top:178px;background:linear-gradient(135deg,#dcdcd8,#f1ece2,#b8a98f)}
.band{position:absolute;left:0;width:1162px}
.band-label{position:absolute;left:0;top:0;width:58px;height:100%;display:flex;align-items:center;justify-content:center}
.band-label span{transform:rotate(-90deg);white-space:nowrap;font-size:16px;color:#fff;letter-spacing:.5px}
.band-body{position:absolute;left:58px;top:0;right:0;height:100%}
.lectures{top:440px;height:344px}
.lectures .band-label{background:var(--navy)}
.lectures .band-body{background:var(--red)}
.lecture{position:absolute;top:78px;text-align:center}
.lecture-tile{width:153px;height:152px;background:#fff;border-radius:16px;display:flex;align-items:center;justify-content:center;margin:0 auto}
.lecture-name{margin-top:20px;font-size:14px;color:var(--red-soft);line-height:1.6}
.theses{top:784px;height:282px}
.theses .band-label{background:var(--blue)}
.theses .band-body{background:var(--pink)}
.theses h2{position:absolute;left:0;right:0;top:22px;text-align:center;font-size:31px;font-weight:400;line-height:1.2;padding-right:54px}
.count{position:absolute;top:70px;width:184px;text-align:center}
.count-bubble{width:184px;height:126px;border-radius:50%;background:#fff;display:flex;align-items:center;justify-content:center;font-size:36px}
.count-label{margin-top:18px;font-size:14px}
.projects{top:1066px;height:571px}
.projects .band-label{background:var(--sky)}
.projects .band-body{background:var(--grey-bg)}
.project-card{position:absolute;width:254px;height:202px;background:#fff;padding-top:22px;text-align:center}
.project-card .cover{height:146px}
.project-card h3{margin-top:12px;font-size:14px;font-weight:500}
.social{top:1637px;height:634px}
.social .band-label{background:var(--ice)}
.social .band-body{background:var(--pink)}
.social-grid{position:absolute;left:108px;top:55px;display:grid;grid-template-columns:repeat(5,163px);grid-template-rows:repeat(3,163px);gap:18px}
.post{position:relative}
.post.big-a{grid-column:1/3;grid-row:1/3}
.post.big-b{grid-column:4/6;grid-row:2/4}
.post .caption{position:absolute;left:0;right:0;bottom:0;height:24px;background:rgba(40,40,40,.6);color:#fff;font-size:14px;text-align:center;line-height:24px}
.post.big-a .caption,.post.big-b .caption{height:88px;line-height:36px}
.tone-a{background:linear-gradient(135deg,#c8c2b8,#8f8a82 55%,#5d5a55)}
.tone-b{background:linear-gradient(135deg,#eae7e2,#b9b2a7 50%,#8e7f70)}
.tone-c{background:linear-gradient(135deg,#63656a,#b6b6b6 55%,#d8d6d2)}
.tone-d{background:linear-gradient(135deg,#8a8680,#d7d4cf 60%,#5b5a57)}
.jobs{top:2271px;height:527px}
.jobs .band-label{background:var(--sky)}
.jobs .band-body{background:#fff}
.job-card{position:absolute;top:128px;width:221px;height:225px}
.job-card .caption{position:absolute;left:0;right:0;bottom:0;height:56px;background:rgba(50,50,50,.65);color:#fff;font-size:10.5px;line-height:1.25;text-align:center;display:flex;align-items:center;justify-content:center;padding:0 10px}
.publications{top:2798px;height:525px}
.publications .band-label{background:var(--pub-blue)}
.publications .band-body{background:var(--red)}
.pub-card{position:absolute;top:135px;width:221px;height:227px;border-radius:14px;background:linear-gradient(135deg,#7a4a3a,#c9b9a6 50%,#6d4c3f);padding:8px}
.pub-card .sheet{height:100%;border-radius:12px;background:rgba(245,240,235,.82);padding:26px 14px;font-size:10.5px;line-height:1.25;text-align:center;color:#555}
.partners{top:3323px;height:245px}
.partners .band-label{background:var(--deep)}
.partners .band-body{background:var(--dark)}
.slider{position:absolute;left:84px;top:92px;width:935px;height:106px;overflow:hidden;display:flex;gap:12px}
.partner{flex:0 0 106px;height:106px;background:#9c9c9c;border:3px solid #777;display:flex;align-items:center;justify-content:center}
.partner i{display:block;width:52px;height:52px;border-radius:50%;background:#6f8fbd}
.partner.alt{border-color:#c35a5e}
.partner.alt i{background:#c35a5e}
.partner.active{background:#fff;border-color:#fff}
.partner.active i{background:var(--brand)}
.arrow{position:absolute;top:137px;width:16px;height:16px;border-radius:50%;background:#111}
.dots{position:absolute;left:0;right:0;top:213px;display:flex;justify-content:center;gap:20px}
.dots i{width:4px;height:4px;border-radius:50%;background:#555}
.site-footer{position:absolute;left:0;top:3568px;width:1200px;height:82px;background:var(--footer)}
.footer-links{position:absolute;left:45px;top:32px;display:flex;gap:18px;font-size:14px;color:#333}
.copyright{position:absolute;right:52px;top:36px;font-size:10px;color:#222}
.edge{position:absolute;left:1162px;top:440px;width:38px;height:3128px;background:var(--edge)}
</style>
</head>
<body>
<header class="site-header">
  <div class="brand"><span class="brand-mark"></span><span class="brand-name">LTN</span></div>
  <nav class="main-nav">
    <span>Research</span><span>Learning-Platform</span><span>Teaching</span><span>Team</span><span>Publications</span><span>Jobs</span><span>Projects</span><span>Events</span><span>Cooperations</span>
    <svg width="13" height="13" viewBox="0 0 13 13"><circle cx="5.5" cy="5.5" r="4" fill="none" stroke="#333" stroke-width="1.8"/><line x1="8.5" y1="8.5" x2="12" y2="12" stroke="#333" stroke-width="1.8"/></svg>
  </nav>
  <div class="university"><span class="university-mark"></span><span class="university-name">UNIVERSITÄT<br>OSTERMARK</span></div>
</header>

<section class="hero">
  <div class="hero-photo" role="img" aria-label="Campus building entrance with large glass facade and outdoor seating"></div>
  <div class="hero-intro">
    <h1>Logistics and Trade Networks<br>(LTN)</h1>
    <p>Chair in Business Administration, especially logistics and trade networks at Ostermark University deals with the development and management of data-driven services, for instance freight and trade. Directed by Prof. Dr.-Ing. Henrik Vollmer, the chair investigates how the application of experimental design methods combined with distributed, data analytic approaches lead to adaptive service designs and innovative solutions. This research is conducted in basic and applied research projects in cooperation with leading research and industry partners. Results are applied and validated in industry projects by the research group Smart Logistics Engineering (SLE) at the Northern Institute for Applied Intelligence (NIAI).</p>
    <p>You can find us now in building B2.7, 3rd floor on the left.</p>
  </div>
  <div class="hero-side top" role="img" aria-label="Students attending a seminar in a classroom"></div>
  <div class="hero-side bottom" role="img" aria-label="Two team members presenting a produce sample at a table"></div>
</section>

<div class="edge"></div>

<section class="band lectures">
  <div class="band-label"><span>LECTURES OF SEMESTER</span></div>
  <div class="band-body">
    <div class="lecture" style="left:72px;width:153px">
      <div class="lecture-tile"><svg width="86" height="76" viewBox="0 0 86 76"><rect x="28" y="2" width="30" height="14" rx="3" fill="none" stroke="var(--icon)" stroke-width="6"/><rect x="2" y="14" width="82" height="26" rx="5" fill="var(--icon)"/><rect x="2" y="44" width="82" height="30" rx="5" fill="var(--icon)"/><rect x="36" y="36" width="14" height="12" rx="2" fill="#fff"/></svg></div>
      <div class="lecture-name">Service Management</div>
    </div>
    <div class="lecture" style="left:352px;width:145px">
      <div class="lecture-tile" style="width:143px"><svg width="70" height="84" viewBox="0 0 70 84"><rect x="10" y="0" width="50" height="80" fill="var(--icon)"/><rect x="2" y="78" width="66" height="6" fill="var(--icon)"/><g fill="#fff"><rect x="20" y="10" width="10" height="10"/><rect x="40" y="10" width="10" height="10"/><rect x="20" y="28" width="10" height="10"/><rect x="40" y="28" width="10" height="10"/><rect x="20" y="46" width="10" height="10"/><rect x="40" y="46" width="10" height="10"/><rect x="29" y="64" width="12" height="16"/></g></svg></div>
      <div class="lecture-name">KI in Unternehmen</div>
    </div>
    <div class="lecture" style="left:623px;width:155px">
      <div class="lecture-tile"><svg width="82" height="64" viewBox="0 0 82 64"><path d="M10 44 Q10 8 41 8 Q72 8 72 44 Z" fill="var(--icon)"/><rect x="34" y="2" width="14" height="26" rx="3" fill="var(--icon)"/><rect x="2" y="48" width="78" height="10" rx="3" fill="var(--icon)"/></svg></div>
      <div class="lecture-name">Service Engineering</div>
    </div>
    <div class="lecture" style="left:862px;width:230px">
      <div class="lecture-tile" style="width:164px"><svg width="92" height="80" viewBox="0 0 92 80"><rect x="4" y="4" width="84" height="54" rx="4" fill="none" stroke="var(--icon)" stroke-width="8"/><rect x="38" y="58" width="16" height="12" fill="var(--icon)"/><rect x="24" y="70" width="44" height="8" rx="2" fill="var(--icon)"/></svg></div>
      <div class="lecture-name">Seminar "Pandemieüber-<br>wachungssysteme" und mobile<br>Apps</div>
    </div>
  </div>
</section>

<section class="band theses">
  <div class="band-label"><span>THESES</span></div>
  <div class="band-body">
    <h2>Open theses in<br>WS 20/21</h2>
    <div class="count" style="left:187px"><div class="count-bubble">1</div><div class="count-label">Bachelor</div></div>
    <div class="count" style="left:737px"><div class="count-bubble">5</div><div class="count-label">Master</div></div>
  </div>
</section>

<section class="band projects">
  <div class="band-label"><span>OUR PROJECTS</span></div>
  <div class="band-body">
    <article class="project-card" style="left:88px;top:55px"><div class="cover tone-c" role="img" aria-label="Hand touching a wall control panel"></div><h3>QUINTAL</h3></article>
    <article class="project-card" style="left:429px;top:55px"><div class="cover" style="background:linear-gradient(135deg,#a8a29a,#6f7c90 50%,#e0dcd4)" role="img" aria-label="Laptop on a desk overlooking a city skyline"></div><h3>Harbor Cloud Ledger</h3></article>
    <article class="project-card" style="left:772px;top:55px"><div class="cover" style="background:linear-gradient(135deg,#3a1f3a,#8a3f72 55%,#d98a4a)" role="img" aria-label="Illuminated wall lettering for projects"></div><h3>PrognoFlux</h3></article>
    <article class="project-card" style="left:88px;top:318px"><div class="cover" style="background:linear-gradient(180deg,#f2f2f2,#cfcac2 55%,#7e7a74)" role="img" aria-label="Stack of papers with colored sticky tabs"></div><h3>Green Field Chain</h3></article>
    <article class="project-card" style="left:429px;top:318px"><div class="cover" style="background:linear-gradient(135deg,#1c1c1c,#8a6a4a 55%,#d8c9b4)" role="img" aria-label="Desk with laptop, cup and keyboard"></div><h3>CARGIN</h3></article>
    <article class="project-card" style="left:772px;top:318px"><div class="cover" style="background:linear-gradient(135deg,#6b4a33,#9a8a7a 50%,#3d3a38)" role="img" aria-label="Laptop showing a dashboard on a leather sofa"></div><h3>VELORA</h3></article>
  </div>
</section>

<section class="band social">
  <div class="band-label"><span>SOCIAL MEDIA</span></div>
  <div class="band-body">
    <div class="social-grid">
      <div class="post big-a tone-b" role="img" aria-label="Person writing in a notebook beside a coffee cup"><div class="caption">Description</div></div>
      <div class="post tone-b" role="img" aria-label="Hand writing with a red pen"><div class="caption">Description</div></div>
      <div class="post tone-c" role="img" aria-label="Hand pointing at a laptop screen"><div class="caption">Description</div></div>
      <div class="post tone-d" role="img" aria-label="Seminar room with presenter"><div class="caption">Description</div></div>
      <div class="post tone-b" role="img" aria-label="Person writing beside a coffee cup"><div class="caption">Description</div></div>
      <div class="post big-b tone-a" role="img" aria-label="Hand writing with a red pen in a notebook"><div class="caption">Description</div></div>
      <div class="post tone-c" role="img" aria-label="Hand pointing at a laptop screen"><div class="caption">Description</div></div>
      <div class="post tone-d" role="img" aria-label="Seminar room with presenter"><div class="caption">Description</div></div>
      <div class="post tone-c" role="img" aria-label="Hand pointing at a laptop screen"><div class="caption">Description</div></div>
    </div>
  </div>
</section>

<section class="band jobs">
  <div class="band-label"><span>JOBS</span></div>
  <div class="band-body">
    <article class="job-card" style="left:44px;background:linear-gradient(135deg,#f2f2f2,#c8cdd6 50%,#5a4030)" role="img" aria-label="Person walking with a leather bag"><div class="caption">NIAI: Research Assistant with a degree in computer science to support the Project Meridian wanted!</div></article>
    <article class="job-card" style="left:309px;background:linear-gradient(135deg,#b84a6a,#5a6ea0 50%,#e0b050)" role="img" aria-label="Busy city street with colorful signs"><div class="caption">UdO: Research Assistant to support Project Management wanted!</div></article>
    <article class="job-card" style="left:574px;background:linear-gradient(135deg,#6a6a6a,#1f2430 50%,#9a9a9a)" role="img" aria-label="Person in a suit on an escalator"><div class="caption">UdO: Research Assistant wanted!</div></article>
    <article class="job-card" style="left:839px;background:linear-gradient(135deg,#e8e8e8,#4a5a6a 50%,#2a6ab0)" role="img" aria-label="Person working at a desk with two monitors"><div class="caption">NIAI: Student assistant in the field of PR and Communication wanted!</div></article>
  </div>
</section>

<section class="band publications">
  <div class="band-label"><span>PUBLICATIONS</span></div>
  <div class="band-body">
    <article class="pub-card" style="left:44px"><div class="sheet">A Context-Aware Smart Freight Service Based On Sensor Data, Proceedings of the 12th Nordic Conference on Trade Systems, 2020.<br>PDF (3.62 MB)</div></article>
    <article class="pub-card" style="left:309px"><div class="sheet">Data-Driven System for Routing of Perishable Goods in Rural Areas, MobiLog '20 Workshop: Learning from Delivery Success Stories: Effective Interventions for Remote Regions, 2020.<br>PDF (2.28 MB)</div></article>
    <article class="pub-card" style="left:574px"><div class="sheet">PD2 : Paired Distances of Load Distributions for the Assessment of Perceived Quality of Route Planning,POSTER presentation at IVPC'20, 2019.<br>PDF (6.98 MB)</div></article>
    <article class="pub-card" style="left:839px"><div class="sheet">International Conference on Logistics &amp; Applications (ICLA 2020) [ed.] Survey on Federated Learning towards Privacy Preserving Supply Chains, , Computer Science Conference Proceedings in Computer Science &amp; Logistics Technology (CS &amp; LT), 2020, pp. 235-253.</div></article>
  </div>
</section>

<section class="band partners">
  <div class="band-label"><span>PARTNERS</span></div>
  <div class="band-body">
    <span class="arrow" style="left:61px"></span>
    <div class="slider">
      <div class="partner alt" style="margin-left:-70px"><i></i></div>
      <div class="partner"><i></i></div>
      <div class="partner"><i></i></div>
      <div class="partner alt"><i></i></div>
      <div class="partner active"><i></i></div>
      <div class="partner"><i></i></div>
      <div class="partner alt"><i></i></div>
      <div class="partner"><i></i></div>
      <div class="partner"><i></i></div>
    </div>
    <span class="arrow" style="left:1025px"></span>
    <div class="dots"><i></i><i></i><i></i><i></i><i></i><i></i><i></i><i></i><i></i></div>
  </div>
</section>

<footer class="site-footer">
  <nav class="footer-links"><span>Contact</span><span>Imprint</span><span>GDPR</span><span>Faculty</span></nav>
  <div class="copyright">© 2020 Chair in Business Administration, esp. Logistics and Trade Networks (LTN)</div>
</footer>
</body>
</html>
```